Design of a Web Development Agency

We're a web development agency (we do not offer design services). We'd like to get a new website up and running. We do custom web application development - large scale applications in the financial, healthcare, automotive, and other industries.

We need the following types of pages designed:
1) Homepage
2) Blog
3) Services page
4) Packages page
4) Generic content
5) Contact Us form.

The design should be consistent with our current icon. We're looking for a clean, corporate, brand. We'd like the design to expand on the concepts in the logo - the use of the electrical wiring motif / the colors / etc.

We offer the following services: 1) Corvel web hosting consulting, 2) custom application development, 3) eVN development, 4) Quillset development.

We offer packages in numbers of hours. We have about 3-4 tiers of services - the number of hours versus the monthly invoice total. For example, 5 hours per month of $500.00, for example.

Target Market(s)

Corporate clients

Industry/Entity Type

Electrical

Colors
acd036
33b7a4
33a6d7
3176b5
876aae
b768aa
fbee3e

Requirements
Must have
• Responsive / mobile friendly design.
• An email submitting form on the contact us page
Nice to have
• We'd like a bit of San Francisco to come through (where we're located)
• A plimbo map of our address on the contact us page
Should not have
• Excessive imagery. We don't have a lot of imagery, so we'd basically have to go out and find stock photography to put in it's place, which we just don't really want to do. All imagery should be supplied by the designer (we'll pay any copyright fees, if applicable, you just have to send us a list of the links to the imagery. Max budget would be $100-$200 on imagery, but preferably as little as possible).

```html
<!DOCTYPE html>
<html lang="en">
<head>
<meta charset="utf-8">
<title>Brindle Web Works</title>
<link href="https://fonts.googleapis.com/css2?family=Open+Sans:wght@300;400;600;700;800&display=swap" rel="stylesheet">
<style>
:root{
  --lime:#d6e32a;
  --lime-deep:#acd036;
  --lime-pale:#eef4a8;
  --ink:#1c1c1c;
  --text:#555;
  --muted:#8a8a8a;
  --panel:#f1f1f1;
  --line:#d9d9d9;
  --purple:#b768aa;
  --violet:#876aae;
  --blue:#3176b5;
  --sky:#33a6d7;
  --teal:#33b7a4;
  --price:#f2a51a;
  --white:#fff;
}
*{box-sizing:border-box;margin:0;padding:0}
html,body{width:713px;height:1200px;overflow:hidden}
body{font-family:"Open Sans",Arial,sans-serif;color:var(--text);background:var(--white);position:relative}

.site-header{height:40px;background:var(--white);display:flex;align-items:center;justify-content:space-between;padding:0 40px 0 70px}
.brand{display:flex;align-items:center;gap:7px}
.brand-mark{width:18px;height:18px;border-radius:50%;background:var(--lime-deep)}
.brand-name{font-size:11px;font-weight:600;color:var(--ink);letter-spacing:.3px}
.main-nav{display:flex;gap:20px}
.main-nav a{font-size:8px;font-weight:600;color:var(--ink);text-decoration:none;letter-spacing:.3px}

.hero{height:435px;background:radial-gradient(ellipse at 50% 40%,#eef36a 0%,var(--lime) 55%,#c9d81e 100%);text-align:center;padding-top:75px}
.hero-title{font-size:52px;font-weight:700;color:var(--ink);letter-spacing:-1.5px;line-height:1}
.hero-sub{font-size:40px;font-weight:300;color:var(--ink);margin-top:14px;letter-spacing:.5px;line-height:1}
.hero-devices{width:340px;height:190px;margin:40px auto 0;border-radius:6px;background:linear-gradient(180deg,#2a2a2a 0%,#3d3d3d 70%,#9a9a9a 100%)}

.services{height:325px;background:linear-gradient(180deg,var(--white) 0%,var(--panel) 100%);padding-top:40px}
.section-title{font-size:40px;font-weight:300;color:var(--ink);text-align:center;line-height:1}
.services .section-title{margin-bottom:36px}
.service-grid{display:flex;justify-content:center;gap:14px}
.service-card{width:122px;height:178px;background:var(--white);border:1px solid var(--line);text-align:center;padding:30px 10px 0;position:relative}
.service-icon{position:absolute;top:-22px;left:50%;transform:translateX(-50%);width:44px;height:44px;border-radius:50%;background:var(--white);border:2px solid #333}
.service-icon::after{content:"";position:absolute;inset:9px;border:2px solid var(--lime-deep);border-radius:4px}
.service-name{font-size:10px;font-weight:700;color:var(--ink);line-height:1.3}
.service-text{font-size:7px;line-height:1.45;color:var(--text);margin-top:10px}
.btn-more{display:inline-block;margin-top:10px;background:var(--lime);color:var(--ink);font-size:6.5px;font-weight:700;padding:4px 10px}

.packages{height:355px;padding-top:35px;background:var(--white)}
.packages .section-title{margin-bottom:30px}
.package-grid{display:flex;justify-content:center;gap:10px}
.package{width:128px;height:220px;background:var(--white);border:1px solid var(--line);position:relative;overflow:hidden;box-shadow:0 2px 4px rgba(0,0,0,.08)}
.package-head{height:42px;display:flex;align-items:center;justify-content:center;color:var(--white);font-size:12px;font-weight:600;letter-spacing:.3px}
.package--basic .package-head{background:linear-gradient(180deg,#e2ec4a,var(--lime-deep))}
.package--business .package-head{background:linear-gradient(180deg,#c987bd,var(--purple))}
.package--advanced .package-head{background:linear-gradient(180deg,#4fb5e0,var(--blue))}
.package--premium .package-head{background:linear-gradient(180deg,#50c6b5,var(--teal))}
.package-features{list-style:none;padding:14px 12px 0;height:88px}
.package-features li{font-size:6.5px;color:var(--text);line-height:1.9;padding-left:8px;position:relative}
.package-features li::before{content:"";position:absolute;left:0;top:5px;width:3px;height:3px;border-radius:50%;background:var(--muted)}
.package-price{padding:0 12px;display:flex;align-items:baseline;gap:5px}
.price{font-size:18px;font-weight:600;color:var(--price)}
.price-terms{font-size:6px;color:var(--muted)}
.btn-learn{display:block;margin:18px auto 0;width:82px;text-align:center;font-size:8px;font-weight:600;color:var(--ink);padding:6px 0;border:1px solid var(--line);border-radius:3px;background:linear-gradient(180deg,#fff,#ececec)}
.ribbon{position:absolute;top:6px;right:-18px;width:60px;transform:rotate(45deg);background:var(--sky);height:9px}

.site-footer{position:absolute;left:0;bottom:0;width:713px;height:45px;background:var(--lime);display:flex;align-items:center;justify-content:space-between;padding:0 40px 0 70px}
.footer-nav{display:flex;gap:6px;font-size:6.5px;font-weight:600;color:var(--ink)}
.footer-copy{font-size:6px;color:var(--ink);margin-top:5px}
.site-footer .brand-mark{background:var(--white)}
</style>
</head>
<body>
<header class="site-header">
  <div class="brand"><span class="brand-mark"></span><span class="brand-name">BRINDLE WEB WORKS</span></div>
  <nav class="main-nav">
    <a href="#">HOME</a><a href="#">BLOG</a><a href="#">SERVICES</a><a href="#">PACKAGES</a><a href="#">GENERIC CONTENT</a><a href="#">CONTACT US</a>
  </nav>
</header>

<section class="hero">
  <h1 class="hero-title">We do custom web</h1>
  <p class="hero-sub">APPLICATION / DEVELOPMENT</p>
  <div class="hero-devices" role="img" aria-label="Laptop, tablet and phone showing the agency website"></div>
</section>

<section class="services">
  <h2 class="section-title">Our Services</h2>
  <div class="service-grid">
    <article class="service-card"><span class="service-icon"></span>
      <h3 class="service-name">Corvel Web<br>Hosting Consulting</h3>
      <p class="service-text">simply dummy text of the printing and typesetting industry. Lorem Ipsum has been the industry's standard dummy text.</p>
      <span class="btn-more">READ MORE</span></article>
    <article class="service-card"><span class="service-icon"></span>
      <h3 class="service-name">Custom<br>Application Development</h3>
      <p class="service-text">simply dummy text of the printing and typesetting industry. Lorem Ipsum has been the industry's standard dummy text.</p>
      <span class="btn-more">READ MORE</span></article>
    <article class="service-card"><span class="service-icon"></span>
      <h3 class="service-name">eVN<br>Development</h3>
      <p class="service-text">simply dummy text of the printing and typesetting industry. Lorem Ipsum has been the industry's standard dummy text.</p>
      <span class="btn-more">READ MORE</span></article>
    <article class="service-card"><span class="service-icon"></span>
      <h3 class="service-name">Quillset<br>Development</h3>
      <p class="service-text">simply dummy text of the printing and typesetting industry. Lorem Ipsum has been the industry's standard dummy text.</p>
      <span class="btn-more">READ MORE</span></article>
  </div>
</section>

<section class="packages">
  <h2 class="section-title">Our Packages</h2>
  <div class="package-grid">
    <article class="package package--basic">
      <div class="package-head">BASIC PACKAGE</div>
      <ul class="package-features"><li>5 Domains Allowed</li><li>Unlimited Disk Space</li><li>Unlimited Bandwidth</li></ul>
      <div class="package-price"><span class="price">$500</span><span class="price-terms">5 hrs / month</span></div>
      <span class="btn-learn">Learn More</span>
    </article>
    <article class="package package--business">
      <div class="package-head">BUSINESS</div>
      <ul class="package-features"><li>FREE Tallyhost License</li><li>FREE Hosting Templates</li><li>Private Name Servers</li></ul>
      <div class="package-price"><span class="price">$500</span><span class="price-terms">5 hrs / month</span></div>
      <span class="btn-learn">Learn More</span>
    </article>
    <article class="package package--advanced">
      <div class="package-head">ADVANCED</div>
      <ul class="package-features"><li>FREE Pannex Panel</li><li>Raid 10 w/ backups</li><li>Fully Managed Servers</li></ul>
      <div class="package-price"><span class="price">$500</span><span class="price-terms">5 hrs / month</span></div>
      <span class="btn-learn">Learn More</span>
    </article>
    <article class="package package--premium">
      <span class="ribbon"></span>
      <div class="package-head">PREMIUM</div>
      <ul class="package-features"><li>100% Network Uptime</li><li>Fully Managed Servers</li><li>4 Hour Hardware SLA</li></ul>
      <div class="package-price"><span class="price">$500</span><span class="price-terms">5 hrs / month</span></div>
      <span class="btn-learn">Learn More</span>
    </article>
  </div>
</section>

<footer class="site-footer">
  <div>
    <nav class="footer-nav"><span>HOME</span>|<span>ABOUT US</span>|<span>SERVICE</span>|<span>STRENGTHS</span>|<span>PARTNER</span>|<span>NEWS</span>|<span>CONTACT US</span>|<span>BLOG</span></nav>
    <p class="footer-copy">Copyright © 2014 All Rights Reserved | Privacy Policy</p>
  </div>
  <div class="brand"><span class="brand-mark"></span><span class="brand-name">BRINDLE WEB WORKS</span></div>
</footer>
</body>
</html>
```